stationary for hygienic company

We need a stationary design for hygienic company which provides public high end sanitary products and high end public lavatory.
We need a fresh and clean style stationary
we want the following things:
* logo (redesigned in eps/vector)
* Letterhead (with company details)
* letterhead (without company details)
* Business card
* note block
* ballpoint
* etcetera (a complete package)

```html
<!DOCTYPE html>
<html lang="en">
<head>
<meta charset="utf-8">
<title>Venella – Stationery Set</title>
<link rel="stylesheet" href="https://fonts.googleapis.com/css2?family=Questrial&family=Roboto+Condensed:wght@400;700&display=swap">
<style>
  :root {
    --magenta: #c8247a;
    --navy: #33357a;
    --cyan: #1e9ad6;
    --ink: #2f2f2f;
    --paper: #ffffff;
    --table: #efefef;
    --rule: #555555;
    --faint: #e6e6e6;
    --brand-font: "Questrial", sans-serif;
    --detail-font: "Roboto Condensed", sans-serif;
  }
  * { box-sizing: border-box; margin: 0; padding: 0; }
  html, body { width: 1200px; height: 795px; overflow: hidden; }
  body { background: var(--table); position: relative; font-family: var(--detail-font); color: var(--ink); }

  .sheet { position: absolute; background: var(--paper); overflow: hidden; }

  /* brand lockup */
  .brand { position: absolute; text-align: center; font-family: var(--brand-font); color: var(--ink); line-height: 1; }
  .brand__row { display: flex; align-items: center; justify-content: center; gap: 4px; }
  .brand__dot { border-radius: 50%; background: var(--magenta); flex: none; }
  .brand__name { font-family: var(--brand-font); }
  .brand__tagline { display: block; font-size: 0.42em; margin-top: 2px; }
  .brand__mark { display: block; font-size: 0.22em; margin-top: 2px; color: #777; }

  /* contact blocks */
  .contact { position: absolute; font-size: 5px; color: var(--navy); font-weight: 700; line-height: 7px; }
  .contact__line { display: flex; align-items: center; gap: 3px; white-space: nowrap; }
  .contact__line svg { width: 5px; height: 5px; fill: var(--magenta); flex: none; }
  .contact__indent { padding-left: 8px; }

  /* letterhead */
  .letterhead { left: 293px; top: 99px; width: 292px; height: 416px; }
  .letterhead .brand { left: 0; right: 0; top: 16px; font-size: 16px; }
  .letterhead__rule { position: absolute; left: 18px; right: 19px; height: 1px; background: var(--rule); }
  .letterhead__rule--top { top: 71px; }
  .letterhead__rule--bottom { top: 378px; }
  .letterhead__graphic { position: absolute; left: 74px; top: 164px; width: 218px; height: 242px; border-radius: 110px 0 0 0; background: linear-gradient(160deg, #e2e2e2, #ececec); }

  /* folder */
  .folder { left: 637px; top: 80px; width: 345px; height: 437px; border-left: 10px solid #f4f4f4; }
  .folder .brand { right: 44px; top: 330px; font-size: 26px; text-align: right; }
  .folder .brand__row { justify-content: flex-end; }

  /* business cards */
  .card { width: 133px; }
  .card--front { left: 186px; top: 549px; height: 77px; }
  .card--back { left: 186px; top: 647px; height: 74px; }
  .card__name { position: absolute; left: 9px; top: 6px; font-size: 7px; font-weight: 700; color: var(--navy); }
  .card__title { position: absolute; left: 9px; top: 14px; font-size: 3.5px; color: var(--magenta); }
  .card--front .contact { left: 9px; top: 31px; font-size: 4px; line-height: 6.5px; }
  .card__tint { position: absolute; right: 0; top: 0; width: 55px; height: 52px; border-radius: 0 0 0 26px; background: linear-gradient(135deg, #f7dbe8, #e8eaf6); }
  .card--front .brand { right: 8px; top: 30px; font-size: 12px; }
  .card__bars { position: absolute; left: 0; right: 0; bottom: 0; height: 3px; display: flex; }
  .card__bars span:first-child { flex: 62; background: var(--magenta); }
  .card__bars span:last-child { flex: 38; background: var(--navy); margin-left: 2px; }
  .card--back .brand { left: 12px; top: 14px; font-size: 13px; }
  .card__graphic { position: absolute; right: 0; top: 0; width: 57px; height: 100%; border-radius: 28px 0 0 28px; background: linear-gradient(90deg, var(--magenta) 0%, var(--navy) 55%, var(--cyan) 100%); }

  /* envelope front */
  .envelope--front { left: 353px; top: 562px; width: 328px; height: 156px; }
  .envelope--front .brand { left: 14px; top: 10px; font-size: 15px; }
  .envelope__graphic { position: absolute; right: 0; top: 0; width: 134px; height: 156px; border-radius: 67px 0 0 67px; background: linear-gradient(90deg, var(--magenta) 0%, var(--magenta) 35%, var(--navy) 60%, var(--cyan) 100%); }

  /* envelope back */
  .envelope--back { left: 713px; top: 562px; width: 328px; height: 156px; }
  .envelope__flap { position: absolute; left: 0; right: 0; top: 0; height: 56px; border-bottom: 1px solid var(--faint); }
  .envelope--back .contact { top: 128px; }
  .envelope__bars { position: absolute; left: 0; right: 0; bottom: 0; height: 4px; display: flex; }
  .envelope__bars span:first-child { flex: 198; background: var(--magenta); }
  .envelope__bars span:last-child { flex: 126; background: var(--navy); margin-left: 4px; }
</style>
</head>
<body>

<svg width="0" height="0" style="position:absolute" aria-hidden="true">
  <defs>
    <symbol id="icon-pin" viewBox="0 0 10 10"><path d="M5 0a3.5 3.5 0 0 0-3.5 3.5C1.5 6 5 10 5 10s3.5-4 3.5-6.5A3.5 3.5 0 0 0 5 0zm0 5a1.5 1.5 0 1 1 0-3 1.5 1.5 0 0 1 0 3z"/></symbol>
    <symbol id="icon-phone" viewBox="0 0 10 10"><path d="M1 3c0-1 1-2 4-2s4 1 4 2v1H7V3H3v1H1zM2 5h6l1 4H1z"/></symbol>
    <symbol id="icon-fax" viewBox="0 0 10 10"><path d="M3 0h4v3H3zM1 4h8v4H1zM3 8h4v2H3z"/></symbol>
    <symbol id="icon-mail" viewBox="0 0 10 10"><path d="M0 2h10v6H0zM0 2l5 3 5-3v1L5 6 0 3z"/></symbol>
    <symbol id="icon-web" viewBox="0 0 10 10"><circle cx="5" cy="5" r="4.5"/></symbol>
  </defs>
</svg>

<!-- Letterhead -->
<section class="sheet letterhead">
  <div class="brand">
    <div class="brand__row"><span class="brand__dot" style="width:7px;height:7px"></span><span class="brand__name">Venella</span></div>
    <span class="brand__tagline">Boutique Hygienique</span>
    <span class="brand__mark">Registered mark</span>
  </div>
  <div class="letterhead__rule letterhead__rule--top"></div>
  <div class="letterhead__graphic" role="img" aria-label="Large faint brand graphic"></div>
  <div class="letterhead__rule letterhead__rule--bottom"></div>
  <div class="contact" style="left:51px;top:386px">
    <div class="contact__line"><svg><use href="#icon-pin"/></svg>Your Commercial or office address</div>
    <div class="contact__indent">in two line</div>
  </div>
  <div class="contact" style="left:132px;top:386px">
    <div class="contact__line"><svg><use href="#icon-phone"/></svg>00.00.00.0000</div>
    <div class="contact__line"><svg><use href="#icon-fax"/></svg>00.00.00.0000</div>
  </div>
  <div class="contact" style="left:185px;top:386px">
    <div class="contact__line"><svg><use href="#icon-mail"/></svg>yourname@yourwebsite.com</div>
    <div class="contact__line"><svg><use href="#icon-web"/></svg>www.yourwebsite.com</div>
  </div>
</section>

<!-- Folder -->
<section class="sheet folder">
  <div class="brand">
    <div class="brand__row"><span class="brand__dot" style="width:10px;height:10px"></span><span class="brand__name">Venella</span></div>
    <span class="brand__tagline">Boutique Hygienique</span>
    <span class="brand__mark">Registered mark</span>
  </div>
</section>

<!-- Business card front -->
<section class="sheet card card--front">
  <div class="card__tint"></div>
  <div class="card__name">Your Name</div>
  <div class="card__title">Job title</div>
  <div class="contact">
    <div class="contact__line"><svg><use href="#icon-pin"/></svg>Your Commercial or office address</div>
    <div class="contact__indent">in two line</div>
    <div class="contact__line"><svg><use href="#icon-phone"/></svg>00.00.00.0000</div>
    <div class="contact__line"><svg><use href="#icon-fax"/></svg>00.00.00.0000</div>
    <div class="contact__line"><svg><use href="#icon-mail"/></svg>yourname@yourwebsite.com</div>
    <div class="contact__line"><svg><use href="#icon-web"/></svg>www.yourwebsite.com</div>
  </div>
  <div class="brand">
    <span class="brand__name">Venella</span>
    <span class="brand__tagline">Boutique Hygienique</span>
  </div>
  <div class="card__bars"><span></span><span></span></div>
</section>

<!-- Business card back -->
<section class="sheet card card--back">
  <div class="brand">
    <div class="brand__row"><span class="brand__dot" style="width:5px;height:5px"></span><span class="brand__name">Venella</span></div>
    <span class="brand__tagline">Boutique Hygienique</span>
  </div>
  <div class="card__graphic" role="img" aria-label="Brand colour graphic"></div>
</section>

<!-- Envelope front -->
<section class="sheet envelope--front">
  <div class="brand">
    <div class="brand__row"><span class="brand__dot" style="width:6px;height:6px"></span><span class="brand__name">Venella</span></div>
    <span class="brand__tagline">Boutique Hygienique</span>
  </div>
  <div class="envelope__graphic" role="img" aria-label="Brand colour graphic"></div>
</section>

<!-- Envelope back -->
<section class="sheet envelope--back">
  <div class="envelope__flap"></div>
  <div class="contact" style="left:40px">
    <div class="contact__line"><svg><use href="#icon-pin"/></svg>Your Commercial or office address</div>
    <div class="contact__indent">in two line</div>
  </div>
  <div class="contact" style="left:152px">
    <div class="contact__line"><svg><use href="#icon-phone"/></svg>00.00.00.0000</div>
    <div class="contact__line"><svg><use href="#icon-fax"/></svg>00.00.00.0000</div>
  </div>
  <div class="contact" style="left:235px">
    <div class="contact__line"><svg><use href="#icon-mail"/></svg>yourname@yourwebsite.com</div>
    <div class="contact__line"><svg><use href="#icon-web"/></svg>www.yourwebsite.com</div>
  </div>
  <div class="envelope__bars"><span></span><span></span></div>
</section>

</body>
</html>
```